Re design current site.

Redesign of the current site. Like current design But I don't own it so I need a custom design similar to the current one. Want the model pictures to be shown off as they currently do on the home page I want to show off contact info make it very noticeable and readable.
Target Market(s)
Males age 30-60
Number of Pages Required
1 page
Requirements
Must have
- Must show off model pictures on the page. Must show contact info easy to read easy to find.

```html
<!DOCTYPE html>
<html lang="en">
<head>
<meta charset="utf-8">
<title>Vexa Models</title>
<link rel="stylesheet" href="https://fonts.googleapis.com/css2?family=Aldrich&family=Open+Sans:wght@400;600&display=swap">
<style>
:root{
  --surround:#2b2a2c;
  --page:#1d1d21;
  --header:#222226;
  --red:#e41e26;
  --white:#ffffff;
  --muted:#8a8a90;
  --line:#34343a;
  --field:#0e0e10;
  --icon:#9a9aa0;
}
*{box-sizing:border-box;margin:0;padding:0}
html,body{width:754px;height:1200px;overflow:hidden}
body{background:radial-gradient(ellipse at 50% 30%,#3a3536 0%,var(--surround) 60%,#1e1d1f 100%);font-family:"Open Sans",sans-serif;color:var(--white);position:relative}
.page{position:absolute;left:94px;top:19px;width:566px;height:1181px;background:var(--page)}
.page *{position:absolute}
.page svg *{position:static}
.header{left:0;top:0;width:566px;height:95px;background:var(--header)}
.logo{left:22px;top:34px;font-family:"Aldrich",sans-serif;font-size:24px;color:var(--red);letter-spacing:.5px;white-space:nowrap;display:flex;align-items:center;gap:8px}
.logo .mark{position:static;width:14px;height:14px;border-radius:50%;background:var(--red)}
.contact-top{left:368px;width:190px}
.contact-top svg{position:absolute;left:0;top:4px}
.contact-top .label{left:22px;top:0;font-family:"Aldrich",sans-serif;font-size:7px;white-space:nowrap}
.contact-top .value{left:22px;top:8px;font-family:"Aldrich",sans-serif;font-size:11.5px;color:#ddd;white-space:nowrap}
.nav{left:0;top:95px;width:566px;height:36px;background:var(--header);border-top:1px solid #2d2d32}
.nav a{top:12px;font-family:"Aldrich",sans-serif;font-size:9.5px;color:#ddd;text-decoration:none}
.social{width:22px;height:22px;border:1px solid #888;border-radius:50%;display:flex;align-items:center;justify-content:center}
.social svg,.foot-social svg{position:static}
.hero{left:0;top:131px;width:566px;height:272px;background:linear-gradient(100deg,#4a3a36 0%,#6a2226 22%,#2a1c22 38%,#151526 60%,#0c0c18 100%)}
.hero-title{left:330px;top:80px;width:125px;height:29px;background:var(--red);font-family:"Aldrich",sans-serif;font-size:15px;line-height:29px;padding-left:9px;white-space:nowrap}
.hero-sub{left:330px;top:112px;width:161px;height:29px;background:#1d1d22;font-size:14px;line-height:29px;padding-left:9px;white-space:nowrap}
.hero-sub svg{position:absolute;right:8px;top:8px}
.dot{top:246px;width:22px;height:2px;background:#fff}
.feature{top:0;width:170px;text-align:center}
.feature .ring{left:47px;top:29px;width:76px;height:76px;border-radius:50%;background:var(--red)}
.feature .ring svg{position:absolute;left:18px;top:12px}
.feature h3{left:0;top:117px;width:170px;font-family:"Aldrich",sans-serif;font-weight:400;font-size:15px}
.feature p{left:12px;top:138px;width:146px;font-size:7.4px;line-height:11.2px;color:var(--muted)}
.rule{background:var(--line)}
.section-title{font-family:"Aldrich",sans-serif;font-size:15.5px;font-weight:400;white-space:nowrap}
.section-title::after{content:"";position:absolute;left:0;top:22px;width:37px;height:2px;background:var(--red)}
.lead{left:31px;top:678px;width:200px;font-size:8.3px;line-height:13px;font-weight:600}
.body-copy{font-size:7.4px;line-height:13.5px;color:var(--muted)}
.btn{background:var(--red);font-family:"Aldrich",sans-serif;font-size:7.5px;text-align:center;color:#fff}
.tile{width:88px;height:66px}
.tile-info{left:255px;top:676px;width:88px;height:66px;background:linear-gradient(#e8353b,#c8242a)}
.tile-info .name{left:0;top:8px;width:88px;text-align:center;font-size:11px}
.tile-info .stats{left:7px;top:30px;font-size:6.3px;line-height:11.5px}
.ad-label{left:0;top:878px;width:566px;text-align:center;font-family:"Times New Roman",serif;font-size:6px}
.ad-left{left:32px;top:887px;width:238px;height:70px;background:#fff;border-top:2px solid var(--red);overflow:hidden}
.ad-left .photo{left:0;top:0;width:140px;height:68px;background:linear-gradient(90deg,#c9a08a,#e8cbbb,#b88a74)}
.ad-left .t1{left:148px;top:4px;font-size:13px;line-height:16px;color:#111;font-weight:600;white-space:nowrap}
.ad-left .t2{left:150px;top:20px;font-size:7.5px;line-height:10px;color:#111;white-space:nowrap}
.ad-left .t2{left:150px}
.ad-left .cta{left:146px;top:33px;width:80px;height:14px;background:var(--red);font-size:7.5px;color:#fff;text-align:center;line-height:14px;border-radius:2px;font-weight:600}
.ad-left .t3{left:150px;top:51px;font-size:7.5px;line-height:10px;color:var(--red);font-weight:600;white-space:nowrap}
.ad-right{left:270px;top:887px;width:265px;height:70px;background:linear-gradient(90deg,#3b2a25,#6d4e43 45%,#3a2a27)}
.ad-right .t1{left:0;top:22px;width:265px;text-align:center;font-family:"Aldrich",sans-serif;font-size:9.5px;letter-spacing:1px;white-space:nowrap}
.ad-right .t2{left:0;top:43px;width:265px;text-align:center;font-size:7px;letter-spacing:1.5px;color:#e6d8d0}
.field{left:31px;top:1067px;width:162px;height:26px;background:var(--field);font-size:6.5px;color:#aaa;line-height:26px;padding-left:9px}
.link{left:256px;font-size:6.6px;color:#ccc;white-space:nowrap}
.link::before{content:"";position:absolute;left:0;top:4px;width:8px;height:1px;background:var(--red)}
.link span{position:static;padding-left:10px}
.c-label{left:361px;font-family:"Aldrich",sans-serif;font-size:8.5px;color:var(--red);white-space:nowrap}
.c-value{left:361px;font-family:"Aldrich",sans-serif;color:#e6e6e6;white-space:nowrap}
.foot-social{width:21px;height:21px;border:1px solid #888;border-radius:50%;top:1110px;display:flex;align-items:center;justify-content:center}
.footer{left:0;top:1155px;width:566px;height:26px;background:var(--red);font-size:6.8px;text-align:center;line-height:26px}
</style>
</head>
<body>
<svg width="0" height="0" style="position:absolute">
  <defs>
    <symbol id="ico-chat" viewBox="0 0 24 24"><path d="M4 5h16v10H10l-4 4v-4H4z" fill="none" stroke="#bbb" stroke-width="2"/></symbol>
    <symbol id="ico-globe" viewBox="0 0 24 24"><g fill="none" stroke="#bbb" stroke-width="2"><circle cx="12" cy="12" r="8"/><path d="M4 12h16M12 4c3 3 3 13 0 16M12 4c-3 3-3 13 0 16"/></g></symbol>
    <symbol id="ico-link" viewBox="0 0 24 24"><g fill="none" stroke="#bbb" stroke-width="2"><path d="M10 14l4-4"/><path d="M8 12l-2 2a3 3 0 0 0 4 4l2-2M16 12l2-2a3 3 0 0 0-4-4l-2 2"/></g></symbol>
    <symbol id="ico-share" viewBox="0 0 24 24"><g fill="none" stroke="#bbb" stroke-width="2"><circle cx="6" cy="12" r="2.5"/><circle cx="18" cy="6" r="2.5"/><circle cx="18" cy="18" r="2.5"/><path d="M8 11l8-4M8 13l8 4"/></g></symbol>
  </defs>
</svg>
<div class="page">
  <header class="header">
    <div class="logo"><span class="mark"></span>VEXA MODELS</div>
    <div class="contact-top" style="top:25px;height:24px">
      <svg width="16" height="16" viewBox="0 0 24 24" fill="none" stroke="#e41e26" stroke-width="1.6"><path d="M5 3h4l2 5-3 2a12 12 0 0 0 6 6l2-3 5 2v4a2 2 0 0 1-2 2A18 18 0 0 1 3 5a2 2 0 0 1 2-2z"/></svg>
      <div class="label">CALL US TODAY</div>
      <div class="value">555 010 2847</div>
    </div>
    <div class="contact-top" style="top:62px;height:24px">
      <svg width="18" height="16" viewBox="0 0 24 20" fill="none" stroke="#e41e26" stroke-width="1.6"><rect x="2" y="4" width="20" height="14"/><path d="M2 4l10 8 10-8M2 18l7-7M22 18l-7-7"/></svg>
      <div class="label">EMAIL US</div>
      <div class="value">hello@vexamodels.com</div>
    </div>
  </header>

  <nav class="nav">
    <a style="left:21px">HOME</a>
    <a style="left:80px">BOOKINGS</a>
    <a style="left:160px">RATES</a>
    <a style="left:202px">MODELS</a>
    <a style="left:258px">EMPLOYMENT</a>
    <a style="left:352px">LINKS</a>
    <span class="social" style="left:431px;top:7px" aria-label="Chat"><svg width="11" height="11"><use href="#ico-chat"/></svg></span>
    <span class="social" style="left:464px;top:7px" aria-label="Website"><svg width="11" height="11"><use href="#ico-globe"/></svg></span>
    <span class="social" style="left:496px;top:7px" aria-label="Link"><svg width="11" height="11"><use href="#ico-link"/></svg></span>
    <span class="social" style="left:529px;top:7px" aria-label="Share"><svg width="11" height="11"><use href="#ico-share"/></svg></span>
  </nav>

  <section class="hero" role="img" aria-label="Photo of a model in a red dress seated in a dim industrial room">
    <div class="hero-title">VEXA MODELS</div>
    <div class="hero-sub">Concierge Service
      <svg width="16" height="13" viewBox="0 0 20 16" fill="none" stroke="#fff" stroke-width="1.4"><path d="M2 2c0 6 4 8 10 8h5M13 6l4 4-4 4"/></svg>
    </div>
    <span class="dot" style="left:248px;background:var(--red)"></span>
    <span class="dot" style="left:272px"></span>
    <span class="dot" style="left:296px"></span>
  </section>

  <section style="left:0;top:403px;width:566px;height:212px">
    <div class="feature" style="left:17px">
      <div class="ring"><svg width="40" height="52" viewBox="0 0 24 30" fill="#fff"><path d="M12 6l2.9 6.5 7.1.7-5.3 4.8 1.5 7L12 21.4 5.8 25l1.5-7L2 13.2l7.1-.7z"/></svg></div>
      <h3>TOP MODLES</h3>
      <p>Ane nulla eram lorem. Summis quo sed legam probant, ab cillum dolor nulla doctrina. Iis dolore officia. Ita ita varias quibusdam, hic offendit.</p>
    </div>
    <div class="feature" style="left:197px">
      <div class="ring" role="img" aria-label="Female model icon"><svg width="40" height="52" viewBox="0 0 40 52" fill="#fff"><circle cx="20" cy="7" r="5"/><path d="M15 14h10l3 12-4 1 4 12H12l4-12-4-1z"/><rect x="15" y="39" width="3.5" height="12"/><rect x="21.5" y="39" width="3.5" height="12"/></svg></div>
      <h3>WOMEN MODLES</h3>
      <p>Ane nulla eram lorem. Summis quo sed legam probant, ab cillum dolor nulla doctrina. Iis dolore officia. Ita ita varias quibusdam, hic offendit.</p>
    </div>
    <div class="feature" style="left:379px">
      <div class="ring" role="img" aria-label="Male model icon"><svg width="40" height="52" viewBox="0 0 40 52" fill="#fff"><circle cx="20" cy="7" r="5"/><path d="M12 14h16l2 16h-4l-1-9v30h-4V33h-2v18h-4V21l-1 9h-4z"/></svg></div>
      <h3>MEN MODLES</h3>
      <p>Ane nulla eram lorem. Summis quo sed legam probant, ab cillum dolor nulla doctrina. Iis dolore officia. Ita ita varias quibusdam, hic offendit.</p>
    </div>
  </section>

  <div class="rule" style="left:0;top:615px;width:566px;height:1px"></div>

  <h2 class="section-title" style="left:32px;top:641px">ABOUT US</h2>
  <p class="lead">Male &amp; female couple available as well.<br>Custom clips and videos available for sale!</p>
  <p class="body-copy" style="left:31px;top:709px;width:180px">VexaModels Concierge Service allows clients to request VexaModels to search for models in the location you plan on traveling to. We will search and find attractive models for the dates requested. We also verify they are interested in the service you expect/request and that the pictures we have are recent and real.</p>
  <div class="btn" style="left:31px;top:817px;width:66px;height:20px;line-height:20px">READ MORE</div>

  <div class="rule" style="left:227px;top:645px;width:1px;height:208px"></div>

  <h2 class="section-title" style="left:256px;top:641px">OUR MODELS</h2>
  <div class="tile-info" role="img" aria-label="Model profile photo with details">
    <div class="name">Sienna</div>
    <div class="stats">Age: 23<br>Height: 5'0<br>Weight: 110</div>
  </div>
  <div class="tile" style="left:351px;top:676px;background:linear-gradient(135deg,#6f88b8,#e6e2e4 50%,#c8a890)" role="img" aria-label="Model photo on white bedding"></div>
  <div class="tile" style="left:446px;top:676px;background:linear-gradient(135deg,#1c2a33,#7a1a20 55%,#2a3038)" role="img" aria-label="Model photo in a red dress"></div>
  <div class="tile" style="left:255px;top:750px;background:linear-gradient(135deg,#e8e8ea,#7a6e6a 50%,#dcdcde)" role="img" aria-label="Model photo in sunglasses"></div>
  <div class="tile" style="left:351px;top:750px;background:linear-gradient(135deg,#121214,#4a3430 50%,#101012)" role="img" aria-label="Model photo in low light"></div>
  <div class="tile" style="left:446px;top:750px;background:linear-gradient(135deg,#bcd0d8,#c84a48 50%,#d8d8dc)" role="img" aria-label="Model photo in a polka dot outfit"></div>
  <div class="btn" style="left:355px;top:833px;width:82px;height:21px;line-height:21px">VIEW ALL MODELS</div>

  <div class="ad-label">Ads by AdLane.net</div>
  <div class="ad-left">
    <div class="photo" role="img" aria-label="Advertisement photo of two women"></div>
    <div class="t1">The Sexy</div>
    <div class="t2">Social Network</div>
    <div class="cta">Join for Free!</div>
    <div class="t3">MatchLounge</div>
  </div>
  <div class="ad-right" role="img" aria-label="Advertisement with a dim portrait">
    <div class="t1">SPARKMATCH MADE FOR GUYS OVER 30</div>
    <div class="t2">SILVERDATES.COM</div>
  </div>

  <h2 class="section-title" style="left:32px;top:986px">JOIN MY NEWSLETTER</h2>
  <p class="body-copy" style="left:31px;top:1017px;width:170px">Voluptate illum dolore ita ipsum, quid labore deserunt singulis, labore admodu multos malis ea nam nam tamen fore</p>
  <div class="field">Enter Your Email ID</div>
  <div class="btn" style="left:31px;top:1105px;width:66px;height:21px;line-height:21px">JOIN NOW!</div>

  <div class="rule" style="left:227px;top:1005px;width:1px;height:150px"></div>

  <h2 class="section-title" style="left:256px;top:986px">GET IN TOUCH</h2>
  <div class="link" style="top:1019px"><span>HOME</span></div>
  <div class="link" style="top:1038px"><span>BOOKINGS</span></div>
  <div class="link" style="top:1057px"><span>RATES</span></div>
  <div class="link" style="top:1077px"><span>MODELS</span></div>
  <div class="link" style="top:1096px"><span>EMPLOYMENT</span></div>
  <div class="link" style="top:1115px"><span>LINKS</span></div>

  <div class="c-label" style="top:1018px">CALL US TODAY</div>
  <div class="c-value" style="top:1028px;font-size:13.5px">555 010 2847</div>
  <div class="c-label" style="top:1056px">EMAIL US</div>
  <div class="c-value" style="top:1066px;font-size:12.5px">hello@vexamodels.com</div>
  <div class="c-label" style="top:1095px">FOLLOW US</div>
  <span class="foot-social" style="left:360px" aria-label="Chat"><svg width="10" height="10"><use href="#ico-chat"/></svg></span>
  <span class="foot-social" style="left:392px" aria-label="Website"><svg width="10" height="10"><use href="#ico-globe"/></svg></span>
  <span class="foot-social" style="left:424px" aria-label="Link"><svg width="10" height="10"><use href="#ico-link"/></svg></span>
  <span class="foot-social" style="left:457px" aria-label="Share"><svg width="10" height="10"><use href="#ico-share"/></svg></span>

  <footer class="footer">Copyright © 2017 VEXA MODELS.&nbsp; All Rights Reserved.</footer>
</div>
</body>
</html>
```